Home page design for a business selling commercial cleaning machines

We need a home page web design for a wholesale business selling commercial and industrial cleaning machines and spare parts. There is a huge range of products but we don't want the home page to be too cluttered and confusing.
- The design needs to be practical and functional - sharp corners, lots of white with just accents/splashes of the business colours.
- This is a link to their holding page which is very very basic - http://www.vornaspec.co.nz/ - use this to get the accent colours but please use lots and lots more WHITE in the home page design! There are no colour codes available.
- The attached HPID (home page design information) is in table boxes just to see placement of information. Information in orange text. Words to go on the design in black text.
- Expected standard of design examples:
http://brimalo-aquaforce.com/
http://brimalointernational.com/
http://tovesk.com/
http://www.mulfin.wb.gs/ (different industry)
- Only use Google fonts. Non-responsive. Width 1100pixels. Header height (without nav bar) 150-160 pixels.
- Will need a PSD of the chosen homepage design (CS5 compatible)

```html
<!DOCTYPE html>
<html lang="en">
<head>
<meta charset="utf-8">
<title>Vornaspec – Commercial Cleaning Machines</title>
<link href="https://fonts.googleapis.com/css2?family=Open+Sans:wght@400;600;700&family=Oswald:wght@400;500;700&display=swap" rel="stylesheet">
<style>
:root{
  --brown:#3a2e29;
  --brown-dark:#2a211d;
  --gold:#c9a23a;
  --ink:#333;
  --muted:#8a8a8a;
  --line:#e2e2e2;
  --field:#f4f4f4;
  --white:#fff;
}
*{box-sizing:border-box;margin:0;padding:0}
html,body{width:730px;height:1200px;overflow:hidden;background:var(--white)}
body{font-family:"Open Sans",Arial,sans-serif;color:var(--ink);font-size:8px;position:relative}
.header{height:84px;position:relative;padding:0 22px}
.brand{position:absolute;left:22px;top:26px;font-family:"Oswald",sans-serif;font-weight:700;font-size:28px;color:var(--brown);letter-spacing:1px}
.header-info{position:absolute;right:22px;top:12px;text-align:right;font-size:7px;color:var(--muted);line-height:1.4}
.phone{position:absolute;right:150px;top:46px;font-family:"Oswald",sans-serif;font-size:12px;color:var(--brown);display:flex;align-items:center;gap:5px}
.search{position:absolute;right:22px;top:44px;width:118px;height:20px;border:1px solid var(--line);font-size:7px;color:var(--muted);padding:5px 6px}
.nav{height:24px;background:var(--brown);display:flex;padding:0 22px}
.nav a{color:var(--white);text-decoration:none;font-size:8px;line-height:24px;padding:0 9px}
.nav a.active{background:var(--gold)}
.hero{position:relative;height:282px}
.hero-img{position:absolute;inset:0;background:linear-gradient(100deg,#d8d3cc 0%,#b9b0a6 45%,#8f7f73 100%)}
.hero-panel{position:absolute;left:400px;top:62px;width:280px;background:rgba(42,33,29,.82);color:var(--white);padding:12px 16px}
.hero-panel h2{font-family:"Oswald",sans-serif;font-weight:400;font-size:15px;margin-bottom:6px}
.hero-panel li{list-style:none;font-size:9px;line-height:1.5}
.arrow{position:absolute;top:128px;width:22px;height:22px;border-radius:50%;background:rgba(255,255,255,.7)}
.arrow.prev{left:10px}.arrow.next{right:10px}
.section-title{font-family:"Oswald",sans-serif;font-weight:500;font-size:14px;text-align:center;margin:26px 0 12px;color:var(--brown-dark)}
.products{display:flex;gap:14px;padding:0 74px}
.product{width:136px}
.product-img{height:108px;background:linear-gradient(#ececec,#bdbdbd)}
.product-name{background:var(--brown);color:var(--white);text-align:center;font-size:8px;line-height:20px}
.features{display:flex;gap:22px;padding:22px 46px 0}
.feature{width:198px}
.feature-img{height:92px}
.feature h3{font-size:9px;font-weight:600;margin:8px 0 4px;color:var(--brown-dark)}
.feature p{font-size:7px;line-height:1.5;color:var(--muted);height:44px}
.btn{display:inline-block;background:var(--gold);color:var(--white);font-size:7px;padding:4px 10px;margin-top:4px}
.contact{border-top:1px solid var(--line);margin:22px 46px 0;padding-top:18px}
.contact h2{font-family:"Oswald",sans-serif;font-weight:400;font-size:13px;color:var(--brown-dark)}
.form{display:grid;grid-template-columns:repeat(3,160px) 1fr;gap:8px 14px;margin-top:14px;align-items:center}
.field{height:20px;background:var(--field);border:1px solid var(--line);font-size:7px;color:var(--muted);padding:5px 6px}
.submit{grid-column:4;grid-row:1/3;justify-self:end;background:var(--gold);color:var(--white);font-size:11px;width:84px;height:30px;line-height:30px;text-align:center}
.partners{display:flex;justify-content:center;gap:28px;margin-top:28px}
.badge{width:110px;height:30px;background:#e6e6e6}
.badge.dark{background:#444}.badge.gold{background:#d9c07a}
.footer{position:absolute;left:0;top:1032px;width:730px;height:168px;background:var(--brown-dark);color:#cfc8c3}
.footer-cols{display:flex;gap:22px;padding:16px 46px 0}
.footer-col{width:150px}
.footer-col h4{font-size:8px;color:var(--white);font-weight:600;margin-bottom:6px;text-transform:uppercase}
.footer-col li{list-style:none;font-size:7px;line-height:1.6}
.social{position:absolute;left:344px;top:112px;display:flex;gap:5px}
.social span{width:12px;height:12px;border-radius:50%;border:1px solid #8c817a}
.footer-bar{position:absolute;bottom:0;left:0;right:0;height:22px;background:#1e1714;font-size:7px;color:#9a908a;display:flex;justify-content:space-between;align-items:center;padding:0 46px}
</style>
</head>
<body>
<header class="header">
  <div class="brand">VORNASPEC</div>
  <div class="header-info">14 Harbour Rd, Tekapo Point · Open to the public<br>Head office Tekapo Point | Distributors NZ wide</div>
  <div class="phone">
    <svg width="12" height="12" viewBox="0 0 24 24"><path d="M6 2h4l2 5-3 2a12 12 0 0 0 6 6l2-3 5 2v4a2 2 0 0 1-2 2A19 19 0 0 1 4 4a2 2 0 0 1 2-2z" fill="#c9a23a"/></svg>
    Call: 04-555 0182
  </div>
  <div class="search">Search</div>
</header>
<nav class="nav">
  <a class="active">Home</a><a>About</a><a>Water blasters</a><a>Drain cleaners</a><a>Custom machines</a><a>Vacuum Cleaners</a><a>Pumps</a><a>Quote</a><a>Contact</a>
</nav>
<section class="hero">
  <div class="hero-img" role="img" aria-label="Person using a commercial vacuum cleaner on a floor"></div>
  <div class="hero-panel">
    <h2>Why Choose Vornaspec?</h2>
    <ul><li>High quality Italian cleaning machines</li><li>Wide range of brands and models</li><li>Specialist knowledge &amp; expert advice</li><li>Huge range of affordable spare parts</li></ul>
  </div>
  <span class="arrow prev"></span><span class="arrow next"></span>
</section>
<h2 class="section-title">HUGE RANGE OF QUALITY CLEANING MACHINES</h2>
<div class="products">
  <div class="product"><div class="product-img" role="img" aria-label="Red water blaster machine"></div><div class="product-name">Water blasters</div></div>
  <div class="product"><div class="product-img" role="img" aria-label="Drain cleaner bottles"></div><div class="product-name">Drain cleaners</div></div>
  <div class="product"><div class="product-img" role="img" aria-label="Custom built cleaning machine"></div><div class="product-name">Custom machines</div></div>
  <div class="product"><div class="product-img" role="img" aria-label="Industrial vacuum cleaner"></div><div class="product-name">Vacuum Cleaners</div></div>
</div>
<div class="features">
  <div class="feature">
    <div class="feature-img" role="img" aria-label="Row of floor cleaning machines" style="background:linear-gradient(#9aa0a6,#5f666c)"></div>
    <h3>Huge Range Of Quality Cleaning Machines</h3>
    <p>Browse our full range of commercial and industrial cleaning machines, built to last and backed by local service and expert advice from our friendly team.</p>
    <span class="btn">Website Specs</span>
  </div>
  <div class="feature">
    <div class="feature-img" role="img" aria-label="Map of New Zealand" style="background:linear-gradient(#cfe0ea,#a9c4b0)"></div>
    <h3>Nationwide Distributors For Sales</h3>
    <p>Our network of distributors covers the whole country, so you can see machines, get demonstrations and find support close to where you work.</p>
    <span class="btn">Contact Now</span>
  </div>
  <div class="feature">
    <div class="feature-img" role="img" aria-label="Metal gears and spare parts" style="background:linear-gradient(#8c8c8c,#3f3f3f)"></div>
    <h3>Comprehensive Range Of Spare Parts</h3>
    <p>We stock a wide range of spare parts for every machine we sell, with fast dispatch and helpful staff to keep your equipment running.</p>
    <span class="btn">Contact Now</span>
  </div>
</div>
<section class="contact">
  <h2>Would you like a Vornaspec representative to contact you? Please fill in the form and we'll be in touch very soon</h2>
  <div class="form">
    <div class="field">Name</div><div class="field">Email address</div><div class="field">Phone</div>
    <div class="submit">Submit</div>
    <div class="field">Company</div><div class="field">Enquiry type</div><div class="field">Message</div>
  </div>
</section>
<div class="partners">
  <span class="badge dark"></span><span class="badge gold"></span><span class="badge"></span><span class="badge"></span>
</div>
<footer class="footer">
  <div class="footer-cols">
    <div class="footer-col"><h4>Navigation</h4><ul><li>Home</li><li>About</li><li>Our Range</li><li>Testimonials</li><li>FAQ</li><li>Contact</li></ul></div>
    <div class="footer-col"><h4>Water Blasters</h4><ul><li>Hot Water Blasters</li><li>Cold Water Blasters</li><li>Cold Water Blasters Electric</li><li>Petrol Water Blasters</li></ul></div>
    <div class="footer-col"><h4>Vacuum Cleaners</h4><ul><li>Dry Vacuum Cleaners</li><li>Wet &amp; Dry Vacuums</li><li>Backpack Vacuums</li></ul></div>
    <div class="footer-col"><h4>Get in Touch</h4><ul><li>14 Harbour Rd, Tekapo Point</li><li>Head office Tekapo Point</li><li>Phone: 04-555 0182</li><li>info@vornaspec.co.nz</li></ul></div>
  </div>
  <div class="social"><span></span><span></span><span></span></div>
  <div class="footer-bar"><span>© Vornaspec. All Rights Reserved.</span><span>Home | Sitemap | Privacy</span></div>
</footer>
</body>
</html>
```